Luxury Business Card Design for High-End Window Treatments

Gilded Vantages
Custom Plantation Shutters & Architectural Shading Systems

⸻

BACK

Daniel Forsythe
Owner

Custom Interior & Exterior Window Treatments

919-482-7034
gildedvantages.com

I have included a picture that I’m hoping we can use on the back, but I’m also wondering if you can get rid of the ladder? Should we get rid of shutters , shades and blinds underneath Gilded Vantages?

Target Market(s)

High-end residential homeowners, custom home builders, architects, interior designers, and luxury renovation clients seeking premium plantation shutters and motorized architectural shading systems.

Industry/Entity Type

Custom Window treatments

Contact Information for Business Card

Front Gilded Vantages Custom Plantation Shutters Motorized Architectural Shading Systems BACK Daniel Forsythe Owner 919-482-7034 GildedVantages.com Custom Interior & Exterior Window Treatments By Appointment

Requirements
Nice to have
• Not 100% sure on nice to halves or the color but you can definitely check out my website to get a better understanding of what I’m trying to do

```html
<!DOCTYPE html>
<html lang="en">
<head>
<meta charset="utf-8">
<title>Gilded Vantages — Business Card</title>
<link rel="stylesheet" href="https://fonts.googleapis.com/css2?family=Tinos:wght@400;700&family=Libre+Baskerville:wght@700&family=Fraunces:opsz,wght@9..144,600&display=swap">
<style>
  :root {
    --page: #1e1e1e;
    --card: #050505;
    --gold: #f2c94c;
    --band: #fbd462;
    --ink: #1a1a1a;
    --cream: #f1ece0;
    --white: #ffffff;
    --sky-top: #4a86d8;
    --sky-low: #a8c7ea;
    --lawn: #6f7a55;
  }
  * { box-sizing: border-box; margin: 0; padding: 0; }
  html, body { width: 1200px; height: 801px; overflow: hidden; }
  body {
    background: var(--page);
    display: flex;
    align-items: center;
    justify-content: center;
    gap: 40px;
    font-family: "Tinos", serif;
  }
  .card {
    position: relative;
    width: 560px;
    height: 320px;
    border-radius: 18px;
    background: var(--card);
    overflow: hidden;
    box-shadow: 0 16px 40px rgba(0,0,0,.55);
  }
  .brand-name {
    font-family: "Tinos", serif;
    font-weight: 400;
    color: var(--cream);
    line-height: 1;
  }
  .brand-lines {
    font-family: "Fraunces", serif;
    font-weight: 600;
    color: var(--gold);
    display: flex;
    gap: 16px;
    white-space: nowrap;
  }

  /* Front */
  .card-front .brand {
    position: absolute;
    left: 120px;
    top: 48px;
  }
  .card-front .brand-name { font-size: 54px; }
  .card-front .brand-name span { display: block; }
  .card-front .brand-name span + span { margin-left: 60px; }
  .card-front .brand-lines { font-size: 20px; margin-top: 12px; margin-left: 40px; }
  .services {
    position: absolute;
    left: 70px;
    top: 222px;
    list-style: none;
    color: var(--white);
    font-size: 22px;
    line-height: 1.35;
    white-space: nowrap;
  }
  .services li::before { content: "•"; margin-right: 10px; }

  /* Back */
  .photo { position: absolute; left: 0; top: 0; }
  .card-back .brand {
    position: absolute;
    left: 300px;
    top: 30px;
  }
  .card-back .brand-name { font-size: 38px; }
  .card-back .brand-name span { display: block; }
  .card-back .brand-name span + span { margin-left: 36px; }
  .card-back .brand-lines { font-size: 14px; gap: 12px; margin-top: 10px; margin-left: 8px; }
  .person { position: absolute; left: 310px; top: 154px; }
  .person-name {
    font-family: "Libre Baskerville", serif;
    font-weight: 700;
    font-size: 24px;
    color: var(--gold);
    white-space: nowrap;
  }
  .person-role { color: var(--white); font-size: 17px; margin: 2px 0 0 12px; }
  .contact { list-style: none; margin: 6px 0 0 12px; }
  .contact li {
    display: flex; align-items: center; gap: 10px;
    color: var(--white); font-size: 17px; line-height: 1.5;
    white-space: nowrap;
  }
  .contact svg { width: 16px; height: 16px; flex: none; }
  .band {
    position: absolute; left: 0; bottom: 0;
    width: 100%; height: 40px;
    padding: 0 24px;
    background: var(--band);
    display: flex; align-items: center; justify-content: center;
    font-family: "Libre Baskerville", serif;
    font-weight: 700;
    font-size: 14px;
    white-space: nowrap;
    color: var(--ink);
  }
</style>
</head>
<body>

<section class="card card-front" aria-label="Card front">
  <div class="brand">
    <p class="brand-name"><span>Gilded</span><span>Vantages</span></p>
    <p class="brand-lines"><span>Shutters</span><span>Shades</span><span>Blinds</span></p>
  </div>
  <ul class="services">
    <li>Custom Plantation Shutters</li>
    <li>Motorized Architectural Shading Systems</li>
  </ul>
</section>

<section class="card card-back" aria-label="Card back">
  <svg class="photo" width="560" height="320" viewBox="0 0 560 320" role="img" aria-label="Photo of a house with a screened porch, lawn and garden chairs">
    <defs>
      <linearGradient id="scene" x1="0" y1="0" x2="0" y2="1">
        <stop offset="0" stop-color="var(--sky-top)"/>
        <stop offset=".35" stop-color="var(--sky-low)"/>
        <stop offset=".5" stop-color="#e9e6df"/>
        <stop offset=".7" stop-color="#4b4d52"/>
        <stop offset="1" stop-color="var(--lawn)"/>
      </linearGradient>
    </defs>
    <polygon points="0,0 240,0 300,280 0,280" fill="url(#scene)"/>
  </svg>

  <div class="brand">
    <p class="brand-name"><span>Gilded</span><span>Vantages</span></p>
    <p class="brand-lines"><span>Shutters</span><span>Shades</span><span>Blinds</span></p>
  </div>

  <div class="person">
    <p class="person-name">Daniel Forsythe</p>
    <p class="person-role">Owner</p>
    <ul class="contact">
      <li>
        <svg viewBox="0 0 16 16" aria-hidden="true"><path d="M4 1.5l2.2 3-1.4 1.6a9 9 0 0 0 5.1 5.1l1.6-1.4 3 2.2-1.3 2.4C8 14.6 1.4 8 1.6 2.8z" fill="var(--gold)"/></svg>
        <span>919-482-7034</span>
      </li>
      <li>
        <svg viewBox="0 0 16 16" aria-hidden="true"><circle cx="8" cy="8" r="6.5" fill="none" stroke="var(--gold)" stroke-width="1.6"/><path d="M1.5 8h13M8 1.5c3 3.5 3 9.5 0 13M8 1.5c-3 3.5-3 9.5 0 13" fill="none" stroke="var(--gold)" stroke-width="1.2"/></svg>
        <span>gildedvantages.com</span>
      </li>
    </ul>
  </div>

  <p class="band">Custom Interior &amp; Exterior Window Treatments By Appointment</p>
</section>

</body>
</html>
```